Wrenmoor Learning Houses MOXIE Poster

We need a poster to put up around our Community/Youth Centers that shows the acronym M.O.X.I.E. which stands for the traits our that make up the culture and personalities of our youth, families and staff. We would like the color scheme to be in our brand colors, and will send them as an upload (grey, blue, green). The poster must have our logo & tagline (uploaded), which may be small and not central. It should have the acronym with the associated words spelled out - as the smaller descriptive words as shown in uploaded attachment. It should be fun - youth friendly (ages 3-18) and really pop. I have also uploaded a sample poster that we created - but don't like....it feels boring, uninspired. It must say "The WLH" M.O.X.I.E as MOXIE is also the name of a different youth agency and we don't want our acronym to be confused with their name. Finally - to tell you a bit more about our organization I have uploaded our annual report. We can't way to see your ideas!!

Target Market(s)

Internal Information Poster for our community centers

Industry/Entity Type

Education

Font styles to use
Other font styles liked:
• FUN

Requirements
Must have
• It must say "The WLH" M.O.X.I.E as MOXIE is also the name of a different youth agency and we don't want our acronym to be confused with their name
• The WLH M.O.X.I.E. - and associated words - should be dominant/prevalent ....
Nice to have
• Fun Images/photos of actual sparks....
Should not have
• As described w/uploads

```html
<!DOCTYPE html>
<html lang="en">
<head>
<meta charset="utf-8">
<title>The WLH M.O.X.I.E. Poster</title>
<link href="https://fonts.googleapis.com/css2?family=Bangers&family=Archivo+Black&display=swap" rel="stylesheet">
<style>
  :root {
    --blue-deep: #1d52a6;
    --blue-mid: #2f6bc3;
    --blue-glow: #4b8de2;
    --green: #8fd53c;
    --green-dark: #4f8a16;
    --grey: #a8aaad;
    --grey-dark: #5f6266;
    --white: #ffffff;
    --white-shade: #9fb3cc;
  }
  html, body {
    margin: 0;
    padding: 0;
    overflow: hidden;
    background: var(--blue-deep);
  }
  .poster {
    position: relative;
    width: 791px;
    height: 1200px;
    overflow: hidden;
    background: radial-gradient(ellipse 70% 55% at 50% 50%, var(--blue-glow) 0%, var(--blue-mid) 55%, var(--blue-deep) 100%);
    font-family: "Bangers", "Comic Sans MS", cursive;
    letter-spacing: 1px;
  }
  .trait-list {
    position: absolute;
    margin: 0;
    padding: 0;
    list-style: none;
    line-height: 0.95;
    text-transform: uppercase;
    white-space: nowrap;
    transform: translate(-50%, -50%) rotate(var(--tilt));
  }
  .trait-list--green { color: var(--green); }
  .trait-list--white { color: var(--white); }

  .traits-drive   { left: 191px; top: 229px; --tilt: -30deg; font-size: 25px; }
  .traits-welcome { left: 632px; top: 240px; --tilt: 62deg;  font-size: 26px; }
  .traits-grit    { left: 424px; top: 836px; --tilt: 0deg;   font-size: 26px; text-align: center; }
  .traits-own     { left: 170px; top: 962px; --tilt: -8deg;  font-size: 25px; }
  .traits-care    { left: 676px; top: 928px; --tilt: -52deg; font-size: 25px; }

  .acronym {
    position: absolute;
    inset: 0;
    pointer-events: none;
  }
  .acronym__org {
    position: absolute;
    left: 200px;
    top: 456px;
    transform: translate(-50%, -50%) rotate(-8deg);
    color: var(--green);
    font-size: 28px;
    text-shadow: 2px 2px 0 var(--green-dark);
  }
  .acronym__letter {
    position: absolute;
    transform: translate(-50%, -50%);
    font-family: "Archivo Black", "Arial Black", sans-serif;
    line-height: 1;
    letter-spacing: -4px;
  }
  .letter--green { color: var(--green); text-shadow: 1px 1px 0 var(--green-dark), 3px 3px 0 var(--green-dark), 5px 5px 0 var(--green-dark), 7px 8px 6px rgba(0,0,0,.45); }
  .letter--grey  { color: var(--grey);  text-shadow: 1px 1px 0 var(--grey-dark), 3px 3px 0 var(--grey-dark), 5px 5px 0 var(--grey-dark), 7px 8px 6px rgba(0,0,0,.45); }
  .letter--white { color: var(--white); text-shadow: 1px 1px 0 var(--white-shade), 3px 3px 0 var(--white-shade), 5px 5px 0 var(--white-shade), 7px 8px 6px rgba(0,0,0,.45); }

  .letter-m { left: 238px; top: 636px; font-size: 150px; }
  .letter-o { left: 318px; top: 552px; font-size: 130px; }
  .letter-x { left: 418px; top: 640px; font-size: 130px; }
  .letter-i { left: 475px; top: 552px; font-size: 130px; }
  .letter-e { left: 555px; top: 616px; font-size: 108px; }

  .acronym__word {
    position: absolute;
    transform: translate(-50%, -50%) rotate(var(--tilt)) skewX(-10deg);
    font-family: "Archivo Black", "Arial Black", sans-serif;
    white-space: nowrap;
    text-shadow: 2px 2px 0 rgba(0,0,0,.35);
  }
  .word--grey  { color: var(--grey); }
  .word--green { color: var(--green); }
  .word--white { color: var(--white); }

  .word-o { left: 420px; top: 460px; --tilt: -35deg; font-size: 34px; }
  .word-i { left: 548px; top: 498px; --tilt: -32deg; font-size: 30px; }
  .word-m { left: 250px; top: 712px; --tilt: -12deg; font-size: 30px; }
  .word-x { left: 452px; top: 712px; --tilt: 0deg;   font-size: 30px; }
  .word-e { left: 648px; top: 628px; --tilt: -14deg; font-size: 28px; }

  .org-mark {
    position: absolute;
    left: 400px;
    top: 1132px;
    display: flex;
    align-items: center;
    gap: 10px;
    color: var(--grey);
    font-size: 26px;
    letter-spacing: 1px;
  }
  .org-mark__dot {
    width: 28px;
    height: 28px;
    border-radius: 50%;
    background: var(--grey);
  }
</style>
</head>
<body>
<main class="poster">
  <ul class="trait-list trait-list--green traits-drive">
    <li>Persistent</li>
    <li>Goal Oriented</li>
    <li>Engaged</li>
    <li>Creative Innovator</li>
  </ul>

  <ul class="trait-list trait-list--white traits-welcome">
    <li>Warm and Welcoming</li>
    <li>Confident Communicator</li>
    <li>Positive Attitude</li>
  </ul>

  <section class="acronym" aria-label="The WLH M.O.X.I.E.">
    <span class="acronym__org">The WLH</span>
    <span class="acronym__word word--grey word-o">ptimistic</span>
    <span class="acronym__word word--green word-i">nventive</span>
    <span class="acronym__letter letter--grey letter-o">O.</span>
    <span class="acronym__letter letter--green letter-i">I.</span>
    <span class="acronym__letter letter--green letter-m">M.</span>
    <span class="acronym__letter letter--white letter-x">X.</span>
    <span class="acronym__letter letter--grey letter-e">E.</span>
    <span class="acronym__word word--white word-m">indful</span>
    <span class="acronym__word word--white word-x">cellent</span>
    <span class="acronym__word word--white word-e">nergetic</span>
  </section>

  <ul class="trait-list trait-list--white traits-grit">
    <li>Resilient</li>
    <li>Resourceful</li>
    <li>Willing</li>
    <li>Critical Thinker</li>
  </ul>

  <ul class="trait-list trait-list--white traits-own">
    <li>Accountable</li>
    <li>Committed</li>
    <li>Self-Regulating</li>
  </ul>

  <ul class="trait-list trait-list--green traits-care">
    <li>Empathetic</li>
    <li>Collaborative</li>
    <li>Helpful</li>
  </ul>

  <div class="org-mark">
    <span class="org-mark__dot"></span>
    <span class="org-mark__name">Wrenmoor Learning Houses</span>
  </div>
</main>
</body>
</html>
```